Pinecrest Real Estate A5 Flyer

A5 Flyer for print distribution.

Front (include attached photo and branding):
Pinecrest are a new face in the Shelley & Rossmoyne real estate market. The Pinecrest team are both Shelley ‘locals’ and are genuinely and sincerely committed to this community. They put people first and pursue exceptional outcomes for their clients. This is the founding vision of Pinecrest.

Values:
Outstanding Customer Service
Timely Communication
Integrity Always
People First
Exceptional Negotiation

If you’re thinking of selling, interested in a free market appraisal, or simply want to find out more about the Pinecrest team, please reach out to Doug or Rowan for a chat. We’d love to shout you a coffee at The Lantern Coffee + Kitchen.

Pinecrest Real Estate
E: hello@pinecrestrealestate-example.com.au
W: pinecrestrealestate-example.com.au

Back (half the page about Doug, other half the page about Rowan). Please include headshots (Rowan is the younger one):

Rowan Ferrabee (Property Consultant):

Rowan has an in-depth understanding of all things property & finance related. With a degree in property & finance, diploma in finance & mortgage broking, certificate IV in real estate practice, project management roles in residential property development, plus years of small business experience as co-founder/co-owner of The Lantern Coffee + Kitchen, his experience in managing competing demands and complex scenarios runs far and wide.

Rowan also has experience in corporate negotiations which is proving to be a very beneficial skill set. Rowan is deeply committed to people and pursuing exceptional outcomes for his clients. He has built a reputation as a man of his word who is genuine and sincere and willing to go above and beyond for his clients.

rowan@pinecrestrealestate-example.com.au
0412 306 248

Doug Penberthy (Director / Licensee):

Doug has worked in various roles inclusive of being a Real Estate Agent, Bank Manager, Financial Counsellor, Mortgage Broker, and previously a Commercial Pilot. He spent eight years in remote Western Australia, where he worked for an international mining company creating strategies to help support the well-being of employees. Doug’s focus in life has always been to help people. To him, it is always about the relationship. Doug gets enormous satisfaction from seeing individuals, families, and businesses thrive financially. He has become a skilled negotiator with extensive experience working for a number of corporations and private firms.
 
What differentiates Doug is his compassion and commitment to people. He works hard to be an excellent communicator with the aim of achieving great results. He  has extensive sales experience with incredible ability to push the boundaries, think outside the box and meet or surpass expectations. This is why his clients keep coming back and continue to refer well into the future. 

doug@pinecrestrealestate-example.com.au
0438 192 607

Target Market(s)

House Sellers / House Buyers

Industry/Entity Type

Real Estate

Colors
0054AA
0677BA
7BADD7
CADEEF
E8F1F8

Requirements
Must have
• Branding / logo, river photo, head shots, company details etc
Nice to have
• Design as per attached branding guide

```html
<!DOCTYPE html>
<html lang="en">
<head>
<meta charset="utf-8">
<title>Pinecrest Real Estate – A5 Flyer</title>
<link rel="stylesheet" href="https://fonts.googleapis.com/css2?family=Archivo+Black&family=Montserrat:wght@400;500;600;700;800&display=swap">
<style>
:root{
  --navy:#17283a;
  --navy-deep:#112032;
  --blue:#0054aa;
  --blue-mid:#0677ba;
  --blue-light:#7badd7;
  --blue-pale:#cadeef;
  --blue-wash:#e8f1f8;
  --ink:#14202c;
  --white:#ffffff;
  --stage:#d9dcdf;
}
*{box-sizing:border-box;margin:0;padding:0}
html,body{width:1200px;height:830px;overflow:hidden}
body{background:var(--stage);font-family:"Montserrat",sans-serif;color:var(--ink);position:relative}
.page{position:absolute;top:67px;width:489px;height:693px;background:var(--white);overflow:hidden;box-shadow:0 12px 24px rgba(0,0,0,.18)}
.front{left:86px}
.back{left:634px}
.abs{position:absolute}

/* brand */
.brand{display:flex;align-items:center;gap:12px}
.brand-dot{width:40px;height:40px;border-radius:50%;background:var(--navy)}
.brand-name{font-family:"Montserrat",sans-serif;font-weight:500;font-size:21px;letter-spacing:6px;color:var(--ink)}

/* front */
.front .brand{left:37px;top:27px}
.intro-kicker{left:42px;top:84px;font-weight:800;font-size:12px;line-height:15px;text-transform:uppercase}
.headline{left:42px;top:120px;font-family:"Archivo Black",sans-serif;font-size:26.5px;line-height:27px;color:var(--blue);text-transform:uppercase}
.intro-copy{left:42px;top:212px;font-size:12px;line-height:15px;width:330px}
.river-photo{left:0;top:247px;width:489px;height:352px;
  background:linear-gradient(180deg,#c9d8e4 0%,#8fb0c6 16%,#4d7aa0 34%,#3f6a88 52%,#2d4a62 70%,var(--navy) 86%,var(--navy) 100%)}
.values{left:42px;top:461px;width:416px;height:96px;border:1.5px solid rgba(255,255,255,.75);border-radius:10px;background:rgba(17,32,50,.55)}
.values-tag{left:33px;top:474px;width:110px;height:27px;background:var(--blue-mid);color:var(--white);border-radius:4px 14px 14px 4px;font-weight:800;font-size:11.5px;display:flex;align-items:center;justify-content:center;box-shadow:0 2px 3px rgba(0,0,0,.4)}
.value{display:flex;align-items:center;gap:9px;color:var(--white);font-size:10px;line-height:11.5px;font-weight:500;text-transform:uppercase}
.value-icon{width:36px;height:36px;border-radius:50%;background:var(--blue-mid);border:2px solid var(--white);flex:none;display:flex;align-items:center;justify-content:center}
.cta-line{left:0;top:568px;width:489px;text-align:center;color:var(--blue-light);font-weight:800;font-size:10.3px;line-height:12px;text-transform:uppercase}
.footer-msg{display:flex;align-items:flex-start;gap:8px;font-weight:800;font-size:12.3px;line-height:14px;text-transform:uppercase}
.footer-msg .hl{color:var(--blue-mid)}
.contact-pill{left:30px;top:661px;width:429px;height:22px;border:1px solid var(--ink);border-radius:11px;display:flex;align-items:center;justify-content:space-between;padding:0 12px;font-size:8.6px;font-weight:500;white-space:nowrap}
.contact-pill span{display:flex;align-items:center;gap:5px;white-space:nowrap}

/* back */
.consultant-panel{left:0;top:0;width:222px;height:693px;background:var(--navy);border-radius:0 42px 42px 0}
.headshot{width:136px;height:136px;border-radius:50%;border:5px solid var(--blue-mid);background:radial-gradient(circle at 50% 40%,#eef1f3 0 40%,#cfd6dc 41%,#9fb0c0 100%)}
.agent-name{font-family:"Archivo Black",sans-serif;font-size:16px;color:var(--blue-mid);text-transform:uppercase;white-space:nowrap}
.agent-role{font-size:9.5px;font-weight:500;margin-top:1px;white-space:nowrap}
.agent-bio{font-size:9.4px;line-height:12.8px}
.agent-bio p+p{margin-top:12.8px}
.phone{font-family:"Archivo Black",sans-serif;font-size:20px;color:var(--blue-mid);display:flex;align-items:center;gap:4px;white-space:nowrap}
.email{font-size:7.6px;display:flex;align-items:center;gap:6px;margin-top:4px;white-space:nowrap}
.rowan{color:var(--white)}
.rowan .agent-role,.rowan .agent-bio,.rowan .email{color:var(--white)}
.rowan .agent-name{font-size:14.5px}
.back .brand{left:246px;top:629px}
.back .brand-dot{width:34px;height:34px}
.back .brand-name{font-size:17px;letter-spacing:5px}
</style>
</head>
<body>

<!-- FRONT -->
<section class="page front">
  <div class="abs brand"><div class="brand-dot"></div><div class="brand-name">PINECREST</div></div>
  <p class="abs intro-kicker">We are new face in the Shelley &amp;<br>Rossmoyne real estate market.</p>
  <h1 class="abs headline">We put people first &amp;<br>pursue exceptional<br>outcomes for clients</h1>
  <p class="abs intro-copy">Our team are both Shelley ‘locals’ and are genuinely and sincerely committed to this community.</p>

  <div class="abs river-photo" role="img" aria-label="Aerial photo of the Swan River foreshore at Shelley with homes and the city skyline"></div>

  <div class="abs values"></div>
  <div class="abs values-tag">OUR VALUES</div>

  <div class="abs value" style="left:158px;top:466px">
    <div class="value-icon"><svg width="18" height="18" viewBox="0 0 18 18" fill="none" stroke="#fff" stroke-width="1.5"><circle cx="9" cy="6" r="3"/><path d="M3 16c1-3 3-4 6-4s5 1 6 4"/></svg></div>
    <span>Outstanding<br>customer service</span>
  </div>
  <div class="abs value" style="left:314px;top:466px">
    <div class="value-icon"><svg width="18" height="18" viewBox="0 0 18 18" fill="none" stroke="#fff" stroke-width="1.5"><path d="M3 7v4h3l6 3V4L6 7z"/><path d="M14 7v4"/></svg></div>
    <span>Timely<br>communication</span>
  </div>
  <div class="abs value" style="left:52px;top:514px">
    <div class="value-icon"><svg width="18" height="18" viewBox="0 0 18 18" fill="none" stroke="#fff" stroke-width="1.5"><path d="M4 9l3 3 7-7"/></svg></div>
    <span>Integrity<br>always</span>
  </div>
  <div class="abs value" style="left:158px;top:514px">
    <div class="value-icon"><svg width="18" height="18" viewBox="0 0 18 18" fill="none" stroke="#fff" stroke-width="1.5"><circle cx="9" cy="5" r="2.5"/><path d="M3 14h12M5 11c1-2 2-3 4-3s3 1 4 3"/></svg></div>
    <span>People first</span>
  </div>
  <div class="abs value" style="left:314px;top:514px">
    <div class="value-icon"><svg width="18" height="18" viewBox="0 0 18 18" fill="none" stroke="#fff" stroke-width="1.5"><path d="M2 9l4-3 3 2 3-2 4 3-5 4-2-1-2 1z"/></svg></div>
    <span>Exceptional<br>negotiation</span>
  </div>

  <p class="abs cta-line">If you’re thinking of selling, interested in a free market<br>appraisal, or simply want to find out more about us</p>

  <div class="abs footer-msg" style="left:42px;top:612px">
    <svg width="28" height="26" viewBox="0 0 28 26" fill="none" stroke="var(--ink)" stroke-width="2"><rect x="2" y="2" width="24" height="16" rx="3"/><path d="M8 18l-2 6 7-6"/><circle cx="9" cy="10" r="1" fill="var(--ink)"/><circle cx="14" cy="10" r="1" fill="var(--ink)"/><circle cx="19" cy="10" r="1" fill="var(--ink)"/></svg>
    <span>Please reach out<br>to <span class="hl">Doug</span> or <span class="hl">Rowan</span><br>for a chat.</span>
  </div>
  <div class="abs footer-msg" style="left:248px;top:612px">
    <svg width="30" height="30" viewBox="0 0 30 30" fill="none" stroke="var(--ink)" stroke-width="2"><path d="M4 14h18v4a7 7 0 0 1-7 7h-4a7 7 0 0 1-7-7z"/><path d="M22 16h3a3 3 0 0 1 0 6h-4"/><path d="M2 27h24"/><path d="M10 3c-1 2 1 3 0 6M15 3c-1 2 1 3 0 6"/></svg>
    <span>We’d love to shout you<br>a coffee at the Lantern<br><span class="hl">Coffee + Kitchen.</span></span>
  </div>

  <div class="abs contact-pill">
    <span><svg width="13" height="10" viewBox="0 0 14 11" fill="none" stroke="var(--blue-mid)" stroke-width="1.5"><rect x="1" y="1" width="12" height="9"/><path d="M1 1l6 5 6-5"/></svg>hello@pinecrestrealestate-example.com.au</span>
    <span><svg width="12" height="12" viewBox="0 0 13 13" fill="none" stroke="var(--blue-mid)" stroke-width="1.3"><circle cx="6.5" cy="6.5" r="5.5"/><ellipse cx="6.5" cy="6.5" rx="2.5" ry="5.5"/><path d="M1 6.5h11"/></svg>pinecrestrealestate-example.com.au</span>
  </div>
</section>

<!-- BACK -->
<section class="page back">
  <div class="abs consultant-panel"></div>

  <div class="abs headshot" style="left:42px;top:42px" role="img" aria-label="Headshot of Rowan Ferrabee"></div>
  <div class="abs headshot" style="left:274px;top:42px" role="img" aria-label="Headshot of Doug Penberthy"></div>

  <div class="abs rowan" style="left:42px;top:207px;width:175px">
    <h2 class="agent-name">Rowan Ferrabee</h2>
    <p class="agent-role">Property Consultant</p>
  </div>
  <div class="abs agent-bio rowan" style="left:42px;top:254px;width:168px">
    <p>Rowan has an in-depth understanding of all things property &amp; finance related. With a degree in property &amp; finance, diploma in finance &amp; mortgage broking, certificate IV in real estate practice, project management roles in residential property development, plus years of small business experience as co-founder/ co-owner of The Lantern Coffee + Kitchen, his experience in managing competing demands and complex scenarios runs far and wide.</p>
    <p>Rowan also has experience in corporate negotiations which is proving to be a very beneficial skill set. Rowan is deeply committed to people and pursuing exceptional outcomes for his clients. He has built a reputation as a man of his word who is genuine and sincere and willing to go above and beyond for his clients.</p>
  </div>
  <div class="abs rowan" style="left:36px;top:602px">
    <div class="phone"><svg width="12" height="20" viewBox="0 0 12 20" fill="none" stroke="var(--blue-mid)" stroke-width="2"><rect x="1" y="1" width="10" height="18" rx="2"/></svg>0412 306 248</div>
    <div class="email" style="padding-left:6px"><svg width="10" height="8" viewBox="0 0 10 8" fill="none" stroke="#fff" stroke-width="1"><rect x=".5" y=".5" width="9" height="7"/><path d="M.5.5l4.5 4 4.5-4"/></svg>rowan@pinecrestrealestate-example.com.au</div>
  </div>

  <div class="abs" style="left:244px;top:203px;width:230px">
    <h2 class="agent-name">Doug Penberthy</h2>
    <p class="agent-role" style="font-weight:600">Director / Licensee</p>
  </div>
  <div class="abs agent-bio" style="left:244px;top:248px;width:228px">
    <p>Doug has worked in various roles inclusive of being a Real Estate Agent, Bank Manager, Financial Counsellor, Mortgage Broker, and previously a Commercial Pilot. He spent eight years in remote Western Australia, where he worked for an international mining company creating strategies to help support the well-being of employees. Doug’s focus in life has always been to help people. To him, it is always about the relationship. Doug gets enormous satisfaction from seeing individuals, families, and businesses thrive financially. He has become a skilled negotiator with extensive experience working for a number of corporations and private firms.</p>
    <p>What differentiates Doug is his compassion and commitment to people. He works hard to be an excellent communicator with the aim of achieving great results. He has extensive sales experience with incredible ability to push the boundaries, think outside the box and meet or surpass expectations. This is why his clients keep coming back and continue to refer well into the future.</p>
  </div>
  <div class="abs" style="left:244px;top:573px">
    <div class="phone"><svg width="12" height="20" viewBox="0 0 12 20" fill="none" stroke="var(--blue-mid)" stroke-width="2"><rect x="1" y="1" width="10" height="18" rx="2"/></svg>0438 192 607</div>
    <div class="email" style="padding-left:6px"><svg width="10" height="8" viewBox="0 0 10 8" fill="none" stroke="var(--blue-mid)" stroke-width="1"><rect x=".5" y=".5" width="9" height="7"/><path d="M.5.5l4.5 4 4.5-4"/></svg>doug@pinecrestrealestate-example.com.au</div>
  </div>

  <div class="abs brand"><div class="brand-dot"></div><div class="brand-name">PINECREST</div></div>
</section>

</body>
</html>
```